Up to the Challenge? Canadian based consulting company needs a two sided business card design

A Canadian based security risk management consulting company needs a two-sided business card design. What we do is provide advice and guidance related to emergency, security and business continuity management for small, medium and large companies to help ensure the protection of their people, assets, information, services, operations and reputation.

The final design should be simple, only one or two colours, eye catching, professional and one that makes people look at three or more times just because it looks so darn good.

I have include examples of business cards I like.

Target Market(s)

Small, medium and large companies.

Industry/Entity Type

Security

Contact Information for Business Card

Business Card Size: Standard size of 3.5" (89mm) x 2.0" (51mm) - (see full specifications and guides on PRINTA's website if required)
Card Stock: Looking to use PRINTA's Velda 32pt stock textured paper - seam colour either chili red or black
Business Name: The Harrowfield Group
Website: www.theharrowfieldgroup.example
Telephone: (555)214-0397
Name: Dana Forsythe
Position: Principle
e-mail: Dana.Forsythe@theharrowfieldgroup.example

Font styles to use
Serif

Colors
ec1f27
000000
9d9d9d
aaaaaa
606060

Requirements
Must have
• - "The Harrowfield Group" logo (see uploaded files). I have included grey scale and colour versions.
• - Business card details (as above)
Nice to have
• - One side black or grey scale.
• - Other side would likely be white.
• - Everyone likes the silver logo on the black background.
• - Small element of colour i.e. red but I'm leaning more to greyscale.
Should not have
• - A lot of colour. Keep it simple.

```html
<!DOCTYPE html>
<html lang="en">
<head>
<meta charset="utf-8">
<title>The Harrowfield Group – Business Card</title>
<link href="https://fonts.googleapis.com/css2?family=Arimo:wght@400;700&display=swap" rel="stylesheet">
<style>
  :root {
    --backdrop: #e4e2df;
    --card-light: #eeeeec;
    --card-dark: #2a2a2b;
    --edge-light: #d9d9d7;
    --ink-dark: #3a3a3c;
    --ink-light: #d6d6d6;
    --ink-muted: #aaaaaa;
  }
  * { box-sizing: border-box; margin: 0; padding: 0; }
  html, body {
    width: 1200px; height: 969px; overflow: hidden;
    background: var(--backdrop);
    font-family: "Arimo", Arial, sans-serif;
  }
  .business-card {
    position: absolute; left: 100px; top: 199px;
    width: 1000px; height: 571px;
    background: var(--card-light);
    box-shadow: 0 14px 40px rgba(0,0,0,.18);
    overflow: hidden;
  }
  .card-shapes { position: absolute; inset: 0; }
  .brand {
    position: absolute; left: 129px; top: 175px; width: 300px;
    display: flex; flex-direction: column; align-items: center; gap: 26px;
  }
  .brand-square {
    width: 104px; height: 104px; background: var(--ink-dark);
  }
  .brand-name {
    color: var(--ink-dark); font-weight: 700; font-size: 34px;
    letter-spacing: 1px; text-align: center; line-height: 1.15;
    text-transform: uppercase;
  }
  .holder {
    position: absolute; right: 26px; top: 70px; text-align: right;
  }
  .holder-name { color: var(--ink-light); font-size: 34px; }
  .holder-title { color: var(--ink-muted); font-size: 25px; margin-top: 6px; }
  .contact-list {
    position: absolute; right: 26px; top: 352px; list-style: none;
    text-align: right; color: var(--ink-muted); font-size: 21px;
  }
  .contact-list li {
    height: 38px; display: flex; justify-content: flex-end; align-items: center; gap: 10px;
  }
  .contact-list .email { font-size: 19px; }
  .contact-icon { width: 22px; height: 22px; flex: none; }
  .handle-square { width: 20px; height: 20px; background: var(--ink-light); flex: none; }
</style>
</head>
<body>
  <div class="business-card">
    <svg class="card-shapes" width="1000" height="571" viewBox="0 0 1000 571">
      <polygon points="448,0 1000,0 1000,571 465,571 625,285" fill="var(--card-dark)"/>
      <polyline points="462,0 640,285 480,571" fill="none" stroke="var(--edge-light)" stroke-width="3"/>
    </svg>

    <div class="brand">
      <div class="brand-square"></div>
      <div class="brand-name">The Harrowfield<br>Group</div>
    </div>

    <div class="holder">
      <div class="holder-name">Dana Forsythe</div>
      <div class="holder-title">Principle</div>
    </div>

    <ul class="contact-list">
      <li>(555)214-0397
        <svg class="contact-icon" viewBox="0 0 24 24"><path fill="var(--ink-light)" d="M3 9c0-3 4-5 9-5s9 2 9 5v2h-5V9c-1-1-7-1-8 0v2H3zM6 12h12l2 8H4z"/><circle cx="12" cy="16" r="2.4" fill="var(--card-dark)"/></svg>
      </li>
      <li>dforsythe <span class="handle-square"></span></li>
      <li class="email">Dana.Forsythe@theharrowfieldgroup.example</li>
      <li>www.theharrowfieldgroup.example</li>
    </ul>
  </div>
</body>
</html>
```